Harwick Quarry Advertising / Price List

Create a 1 page document for print and email showcasing what we have available in our Quarry. Bottom of sample should have the information included and then the rest of the document focus on items and services available with the quarry. The top section will need room to list about items below and have about 5 pictures that I am working on getting.

Materials Available for Pick Up and/or Delivery:
Recycled Breaker Run
3/4" & 1 1/4" Crushed Recycled Asphalt
1 1/4" Crushed Recycled Stone
1 1/4" Screened "Built To Last Mix"
3/4" Clean Stone
3/8" Washed Pea Stone
Mound Sand
Fill Sand Material
Fill/Clay Fill Material
Compost
Peot Moss
Topsoil
Reclaimed Cream City Bricks

Dumping of Materials with Approval:
Clean Concrete
Dirty and / or Large Concrete or Vextomar
Clean Brick
Asphalt
Fill Material
Brush and / or Stumps
Hydro Vac Slurry Dumping

Target Market(s)

Contractors in our area

Industry/Entity Type

Trucking & Excavation

Colors
EB3D1F
EC4F4E
F09395
F8D3D4
FCEDEE

Requirements
Must have
• Similar Look & Feel as Sample Copy

```html
<!DOCTYPE html>
<html lang="en">
<head>
<meta charset="utf-8">
<title>Harwick Quarry – Materials &amp; Services</title>
<link href="https://fonts.googleapis.com/css2?family=Oswald:wght@500&family=Open+Sans:wght@600;700&family=Montserrat:wght@700;800&display=swap" rel="stylesheet">
<style>
  :root {
    --red: #EB3D1F;
    --red-deep: #D8222A;
    --red-dark: #9A1A20;
    --coral: #EC4F4E;
    --pink: #F09395;
    --blush: #F8D3D4;
    --mist: #FCEDEE;
    --ink: #111111;
    --white: #ffffff;
  }
  * { margin: 0; padding: 0; box-sizing: border-box; }
  html, body { width: 846px; height: 1200px; overflow: hidden; background: var(--mist); }
  .sheet {
    position: relative; width: 846px; height: 1200px; overflow: hidden;
    background: linear-gradient(180deg, var(--red-deep) 0%, var(--coral) 60%, var(--red-deep) 100%);
    font-family: 'Oswald', sans-serif;
  }
  .hero-photo {
    position: absolute; left: 0; top: 0; width: 846px; height: 620px;
    background: linear-gradient(180deg, #9fb3c8 0%, #7d7466 28%, #c9302c 45%, #d8342f 62%, #b8b2a8 100%);
  }
  .swoosh { position: absolute; left: 0; top: 0; }
  .brand-disc {
    position: absolute; left: 423px; top: -121px; width: 450px; height: 450px;
    border-radius: 50%; background: var(--red-deep);
  }
  .brand {
    position: absolute; left: 540px; top: 95px; width: 270px; text-align: center; color: var(--white);
    font-family: 'Montserrat', sans-serif; font-weight: 800;
  }
  .brand-name { font-size: 34px; letter-spacing: 1px; line-height: 1; }
  .brand-tag { font-size: 6px; font-weight: 700; margin-top: 6px; letter-spacing: .2px; }
  .brand-sub { font-size: 10px; font-weight: 700; margin-top: 4px; }
  .headline {
    position: absolute; left: 520px; top: 192px; width: 300px; text-align: center;
    color: var(--white); font-size: 24px; line-height: 29px;
  }
  .materials-panel {
    position: absolute; left: 56px; top: 397px; width: 734px; height: 441px;
    border-radius: 22px; background: rgba(130, 16, 24, .82);
  }
  .pill {
    position: absolute; height: 36px; border-radius: 18px; background: var(--blush);
    color: var(--ink); font-size: 21px; line-height: 36px; text-align: center;
  }
  .pill-pickup { left: 127px; top: 20px; width: 479px; }
  .pill-dump { left: 132px; top: 275px; width: 479px; }
  .list { position: absolute; list-style: none; color: var(--white); font-size: 20px; line-height: 27px; }
  .list-pickup-left { left: 32px; top: 74px; }
  .list-pickup-right { right: 46px; top: 70px; text-align: right; }
  .list-dump-left { left: 34px; top: 320px; }
  .list-dump-right { right: 46px; top: 320px; text-align: right; }
  .services-card {
    position: absolute; left: 63px; top: 854px; width: 719px; height: 193px;
    border-radius: 18px; background: var(--white);
  }
  .services-title {
    position: absolute; left: 0; top: 6px; width: 100%; text-align: center;
    font-family: 'Open Sans', sans-serif; font-weight: 700; font-size: 23px; color: var(--ink);
  }
  .service {
    position: absolute; top: 895px; width: 170px; text-align: center;
    font-family: 'Open Sans', sans-serif; font-weight: 700; font-size: 17px; line-height: 20px; color: var(--ink);
    display: flex; align-items: center; justify-content: center; height: 42px;
  }
  .service-photo {
    position: absolute; top: 948px; width: 156px; height: 156px; border-radius: 50%;
    border: 4px solid var(--white); box-shadow: 0 2px 6px rgba(0,0,0,.25);
  }
  .photo-brush { background: linear-gradient(160deg, #5f8a3a, #d8b32a 55%, #7fae3c); }
  .photo-excavate { background: linear-gradient(180deg, #8fc0ea, #e0c23a 45%, #6b4630); }
  .photo-snow { background: linear-gradient(180deg, #c9ccd2, #8d8f94 45%, #f4f5f7 70%); }
  .photo-truck { background: linear-gradient(180deg, #9dc4e6, #b8bcc0 45%, #8a7e70); }
  .footer { position: absolute; top: 1128px; left: 0; width: 846px; color: var(--blush);
    font-family: 'Open Sans', sans-serif; font-weight: 600; font-size: 14px; line-height: 19px; }
  .footer b { color: var(--white); font-weight: 600; }
  .contact { position: absolute; display: flex; align-items: center; gap: 8px; }
  .divider { position: absolute; top: 0; width: 1px; height: 46px; background: var(--mist); }
  .icon { width: 18px; height: 18px; flex: none; }
</style>
</head>
<body>
<main class="sheet">
  <div class="hero-photo" role="img" aria-label="Fleet of red roll-off dumpsters and red roll-off trucks in the quarry yard beside a river"></div>

  <svg class="swoosh" width="846" height="1200" viewBox="0 0 846 1200" aria-hidden="true">
    <path d="M0 345 C220 470 560 610 846 600 L846 1200 L0 1200 Z" fill="#D8222A" opacity=".95"/>
    <path d="M0 420 C260 560 560 660 846 640 L846 1200 L0 1200 Z" fill="#EC4F4E" opacity=".55"/>
    <path d="M0 440 C300 600 620 760 846 800 C600 720 300 620 0 500 Z" fill="#9A1A20" opacity=".6"/>
  </svg>

  <div class="brand-disc"></div>
  <div class="brand">
    <div class="brand-name">HARWICK</div>
    <div class="brand-tag">BRUSH CUTTING . EXCAVATING . SNOW REMOVAL . TRUCKING</div>
    <div class="brand-sub">QUARRY, LLC · OAKMONT, WI</div>
  </div>
  <h1 class="headline" style="font-weight:500">Now Offering<br>Commercial and Residential<br>Roll Off Services</h1>

  <section class="materials-panel">
    <h2 class="pill pill-pickup" style="font-weight:500">Materials Available for Pick Up and/or Delivery</h2>
    <ul class="list list-pickup-left">
      <li>Recycled Breaker Run</li>
      <li>3/4" &amp; 1 1/4" Crushed Recycled Asphalt</li>
      <li>1 1/4" Crushed Recycled Stone</li>
      <li>1 1/4" Screened "Built To Last Mix"</li>
      <li>3/4" Clean Stone</li>
      <li>3/8" Washed Pea Stone</li>
      <li>Mound Sand</li>
    </ul>
    <ul class="list list-pickup-right">
      <li>Fill Sand Material</li>
      <li>Fill/Clay Fill Material</li>
      <li>Compost</li>
      <li>Peot Moss</li>
      <li>Topsoil</li>
      <li>Reclaimed Cream City Bricks</li>
    </ul>
    <h2 class="pill pill-dump" style="font-weight:500">Dumping of Materials with Approval</h2>
    <ul class="list list-dump-left">
      <li>Clean Concrete</li>
      <li>Dirty and / or Large Concrete or Vextomar</li>
      <li>Clean Brick</li>
      <li>Asphalt</li>
    </ul>
    <ul class="list list-dump-right">
      <li>Fill Material</li>
      <li>Brush and / or Stumps</li>
      <li>Hydro Vac Slurry Dumping</li>
    </ul>
  </section>

  <section class="services-card">
    <h2 class="services-title">Our Commercial and Residential Services Include</h2>
  </section>
  <div class="service" style="left:74px">Brush Cutting</div>
  <div class="service" style="left:248px">Excavating</div>
  <div class="service" style="left:420px">Snow Plowing<br>and Removal</div>
  <div class="service" style="left:598px">Trucking</div>
  <div class="service-photo photo-brush" style="left:81px" role="img" aria-label="Excavator with mulching head clearing brush"></div>
  <div class="service-photo photo-excavate" style="left:255px" role="img" aria-label="Yellow excavator digging soil"></div>
  <div class="service-photo photo-snow" style="left:427px" role="img" aria-label="Loaders plowing snow in a parking lot"></div>
  <div class="service-photo photo-truck" style="left:605px" role="img" aria-label="Red semi truck hauling a trailer at a site"></div>

  <footer class="footer">
    <div class="contact" style="left:70px; top:8px; align-items:flex-start">
      <svg class="icon" viewBox="0 0 18 18"><circle cx="9" cy="9" r="8.5" fill="none" stroke="#F8D3D4"/><path d="M9 4a3 3 0 0 0-3 3c0 2.5 3 6 3 6s3-3.5 3-6a3 3 0 0 0-3-3z" fill="#F8D3D4"/><circle cx="9" cy="7" r="1.1" fill="#D8222A"/></svg>
      <span>1480 Ridgeline Road<br>Oakmont, WI 54900</span>
    </div>
    <div class="divider" style="left:243px"></div>
    <div class="contact" style="left:275px; top:0">
      <svg class="icon" viewBox="0 0 18 18"><circle cx="9" cy="9" r="8.5" fill="none" stroke="#F8D3D4"/><rect x="4.5" y="6" width="9" height="6.5" fill="none" stroke="#F8D3D4"/><path d="M4.5 6l4.5 3.6L13.5 6" fill="none" stroke="#F8D3D4"/></svg>
      <span>dispatch@<b>harwickquarry</b>.com</span>
    </div>
    <div class="contact" style="left:275px; top:27px">
      <svg class="icon" viewBox="0 0 18 18"><circle cx="9" cy="9" r="8.5" fill="none" stroke="#F8D3D4"/><circle cx="9" cy="9" r="4.8" fill="none" stroke="#F8D3D4"/><path d="M4.2 9h9.6M9 4.2c-2 2.6-2 7 0 9.6M9 4.2c2 2.6 2 7 0 9.6" fill="none" stroke="#F8D3D4"/></svg>
      <span>www.<b>harwickquarry</b>.com</span>
    </div>
    <div class="divider" style="left:548px"></div>
    <div class="contact" style="left:580px; top:2px">
      <svg class="icon" viewBox="0 0 18 18"><circle cx="9" cy="9" r="8.5" fill="none" stroke="#F8D3D4"/><path d="M6 4.5l1.8 2.2-1 1.3c.6 1.4 1.8 2.6 3.2 3.2l1.3-1 2.2 1.8-1 1.5c-3.6-.2-7-3.6-7.2-7.2z" fill="#F8D3D4"/></svg>
      <span>Call or Text <b>555-201-4870</b></span>
    </div>
    <div class="contact" style="left:580px; top:29px">
      <svg class="icon" viewBox="0 0 18 18"><circle cx="9" cy="9" r="8.5" fill="none" stroke="#F8D3D4"/><rect x="4.5" y="7.5" width="9" height="4.5" fill="#F8D3D4"/><rect x="6" y="4.5" width="6" height="3" fill="none" stroke="#F8D3D4"/><rect x="6" y="11" width="6" height="2.5" fill="#D8222A" stroke="#F8D3D4" stroke-width=".8"/></svg>
      <span>Fax <b>555-201-4871</b></span>
    </div>
  </footer>
</main>
</body>
</html>
```